I need a business card.

I need a simple, minimalist, business card. I think the coolest business card I have ever seen is Marty Vexler's from Kestrel's 9... it is just a little creepy for the real world.
I am a photographer and I need a card that I can give to brides or potential portrait customers that is simple and classy.
My name is Glen Hardesty. My website is www.glenhardesty-example.com
Please design my card.
I think it could be as simple as my name, phone # and website... where the rest of my contact could be found... or maybe my email and no website... I am open to ideas. I imagined the card on thick card stock with a black background...

```html
<!DOCTYPE html>
<html lang="en">
<head>
<meta charset="utf-8">
<title>Glen Hardesty — Business Card</title>
<link rel="stylesheet" href="https://fonts.googleapis.com/css2?family=Josefin+Sans:wght@400;600;700&family=Cormorant+Garamond:wght@500&display=swap">
<style>
  :root {
    --page-bg: #d6d6d6;
    --dark-card: #161616;
    --dark-card-edge: #0c0c0c;
    --dark-frame: #bdbdbd;
    --dark-text: #d9d9d9;
    --dark-muted: #9a9a9a;
    --light-card: #e4e4e4;
    --light-frame: #4a4a4a;
    --light-text: #5a5a5a;
    --light-muted: #7a7a7a;
    --label: #333333;
  }
  * { margin: 0; padding: 0; box-sizing: border-box; }
  html, body { width: 1059px; height: 1200px; overflow: hidden; }
  body {
    position: relative;
    background: var(--page-bg);
    font-family: "Josefin Sans", sans-serif;
  }
  .card {
    position: absolute;
    width: 506px;
    height: 303px;
    border-radius: 30px;
    overflow: hidden;
  }
  .card--dark { background: radial-gradient(ellipse at 50% 45%, #262626 0%, var(--dark-card) 55%, var(--dark-card-edge) 100%); }
  .card--light { background: radial-gradient(ellipse at 50% 45%, #ececec 0%, var(--light-card) 60%, #dadada 100%); }
  .card__frame {
    position: absolute;
    left: 55px; top: 33px;
    width: 398px; height: 237px;
    overflow: visible;
  }
  .card--dark .card__frame path { stroke: var(--dark-frame); }
  .card--light .card__frame path { stroke: var(--light-frame); }
  .card__frame path { fill: none; stroke-width: 1.4; }
  .card__content {
    position: absolute;
    inset: 0;
    text-align: center;
  }
  .card--back .card__content { transform: scaleX(-1); opacity: 0.75; }
  .card__name {
    position: absolute;
    left: 0; right: 0; top: 122px;
    font-size: 25px;
    font-weight: 700;
    letter-spacing: 2.5px;
    line-height: 1;
  }
  .card__title {
    position: absolute;
    left: 0; right: 0; top: 154px;
    font-size: 10.5px;
    font-weight: 400;
    letter-spacing: 2.2px;
  }
  .card__contact {
    position: absolute;
    left: 0; right: 0; top: 212px;
    font-size: 11px;
    letter-spacing: 1.2px;
    display: flex;
    justify-content: center;
    align-items: center;
    gap: 14px;
  }
  .card__dot { width: 5px; height: 5px; border-radius: 50%; }
  .card--dark .card__name, .card--dark .card__contact { color: var(--dark-text); }
  .card--dark .card__title { color: var(--dark-muted); }
  .card--dark .card__dot { background: var(--dark-muted); }
  .card--light .card__name, .card--light .card__contact { color: var(--light-text); }
  .card--light .card__title { color: var(--light-muted); }
  .card--light .card__dot { background: var(--light-muted); }
  .side-label {
    position: absolute;
    font-family: "Cormorant Garamond", serif;
    font-size: 14px;
    letter-spacing: 2.5px;
    color: var(--label);
  }
</style>
</head>
<body>
  <svg width="0" height="0" style="position:absolute">
    <defs>
      <g id="notched-frame">
        <path d="M22,0 H376 A22 22 0 0 0 398,22 V215 A22 22 0 0 0 376,237 H22 A22 22 0 0 0 0,215 V22 A22 22 0 0 0 22,0 Z"/>
        <path d="M26,4 H372 A22 22 0 0 0 394,26 V211 A22 22 0 0 0 372,233 H26 A22 22 0 0 0 4,211 V26 A22 22 0 0 0 26,4 Z"/>
      </g>
    </defs>
  </svg>

  <!-- Dark set -->
  <div class="card card--dark card--front" style="left:16px; top:266px;">
    <svg class="card__frame" viewBox="0 0 398 237"><use href="#notched-frame"/></svg>
    <div class="card__content">
      <div class="card__name">GLEN HARDESTY</div>
      <div class="card__title">PHOTOGRAPHER</div>
      <div class="card__contact"><span>555.014.2290</span><span class="card__dot"></span><span>WWW.GLENHARDESTY-EXAMPLE.COM</span></div>
    </div>
  </div>
  <div class="card card--dark card--back" style="left:531px; top:266px;">
    <svg class="card__frame" viewBox="0 0 398 237"><use href="#notched-frame"/></svg>
    <div class="card__content">
      <div class="card__name">GLEN HARDESTY</div>
      <div class="card__title">PHOTOGRAPHER</div>
      <div class="card__contact"><span>555.014.2290</span><span class="card__dot"></span><span>WWW.GLENHARDESTY-EXAMPLE.COM</span></div>
    </div>
  </div>
  <div class="side-label" style="left:58px; top:604px;">FRONT</div>
  <div class="side-label" style="left:582px; top:604px;">BACK</div>

  <!-- Light set -->
  <div class="card card--light card--front" style="left:16px; top:790px;">
    <svg class="card__frame" viewBox="0 0 398 237"><use href="#notched-frame"/></svg>
    <div class="card__content">
      <div class="card__name">GLEN HARDESTY</div>
      <div class="card__title">PHOTOGRAPHER</div>
      <div class="card__contact"><span>555.014.2290</span><span class="card__dot"></span><span>WWW.GLENHARDESTY-EXAMPLE.COM</span></div>
    </div>
  </div>
  <div class="card card--light card--back" style="left:531px; top:790px;">
    <svg class="card__frame" viewBox="0 0 398 237"><use href="#notched-frame"/></svg>
    <div class="card__content">
      <div class="card__name">GLEN HARDESTY</div>
      <div class="card__title">PHOTOGRAPHER</div>
      <div class="card__contact"><span>555.014.2290</span><span class="card__dot"></span><span>WWW.GLENHARDESTY-EXAMPLE.COM</span></div>
    </div>
  </div>
  <div class="side-label" style="left:58px; top:1128px;">FRONT</div>
  <div class="side-label" style="left:582px; top:1128px;">BACK</div>
</body>
</html>
```